High end business card design for custom homebuilding company

Looking for a high end business card design that is unique and elegant. Can use embossing, foil printing, laser die cutting, or any high end printing technique or high end paper. Will upload current design so you can see the logo and what we are using currently, but we want something more unique and elegant. I included our logo to help with design.

Target Market(s)

High end custom home buyers of $1.5 million plus homes. Also real estate developers of high end communities.

Industry/Entity Type

Business

Contact Information for Business Card

Double sided. We want something very elegant and expensive looking. We are looking to incorporate a combination of perhaps linen paper or a high end paper, with foil stamping or embossing/debossing to make the card look unique, but still elegant. We tend to use blacks and golds, but are open to any ideas. Looking for creative and unique design.

Colors

Designer to choose colors to be used in the design.

Requirements
Must have
• High end, elegant look. Can use foil, embossing, or high end papers like linen. We want to make the card unique and interesting, but elegant and expensive looking.
Nice to have
• I am including just some cards I saw that looked interesting for one reason or another. I like a clean elegant design and like both the clean white style, and the blacks. So not sure if we want a black design or white. Would like to see both.

```html
<!DOCTYPE html>
<html lang="en">
<head>
<meta charset="utf-8">
<title>Aldergate Custom Homes – Business Card</title>
<link rel="stylesheet" href="https://fonts.googleapis.com/css2?family=Tinos:wght@400;700&display=swap">
<style>
  :root {
    --bg: #e9ecec;
    --paper: #f7f7f6;
    --ink: #1b1b1b;
    --gold: #b08a1e;
    --gold-light: #d8bc4a;
    --grey: #8a8a8a;
    --rule: #9a9a9a;
  }
  * { margin: 0; padding: 0; box-sizing: border-box; }
  html, body { width: 1200px; height: 900px; overflow: hidden; }
  body {
    background: var(--bg);
    font-family: "Tinos", "Times New Roman", serif;
    color: var(--ink);
    display: flex;
    align-items: center;
    justify-content: center;
    gap: 40px;
  }
  .card {
    width: 540px;
    height: 309px;
    background: var(--paper);
    box-shadow: 0 2px 6px rgba(0,0,0,0.12);
    position: relative;
  }
  /* Front */
  .card--front {
    display: flex;
    align-items: center;
    justify-content: center;
  }
  .brand {
    display: flex;
    align-items: center;
    gap: 12px;
  }
  .brand__dot {
    width: 26px; height: 26px;
    border-radius: 50%;
    background: var(--gold);
  }
  .brand__name {
    font-size: 30px;
    font-weight: 400;
    letter-spacing: 2px;
    color: var(--ink);
    line-height: 1;
  }
  /* Back */
  .card--back { overflow: hidden; }
  .frame {
    position: absolute;
    inset: 14px;
    border: 18px solid transparent;
    border-image: linear-gradient(135deg, var(--gold-light) 0%, var(--gold) 40%, #6b5a22 60%, var(--ink) 80%) 1;
  }
  .details {
    position: absolute;
    inset: 32px;
    display: flex;
    flex-direction: column;
    align-items: center;
    justify-content: center;
    text-align: center;
  }
  .details__name {
    font-size: 19px;
    color: var(--gold);
    letter-spacing: 1px;
  }
  .details__title {
    font-size: 12px;
    font-weight: 700;
    letter-spacing: 0.5px;
    margin-top: 2px;
  }
  .divider {
    display: flex;
    align-items: center;
    gap: 8px;
    width: 320px;
    margin: 10px 0 8px;
  }
  .divider__line { flex: 1; height: 1px; background: var(--rule); }
  .social { display: flex; gap: 4px; }
  .social__item { width: 17px; height: 17px; border-radius: 50%; background: var(--ink); }
  .details__address { font-size: 11px; color: var(--grey); }
  .contact {
    font-size: 11px;
    color: var(--grey);
    margin-top: 3px;
    display: flex;
    align-items: center;
    gap: 4px;
  }
  .contact svg { width: 10px; height: 10px; fill: var(--gold); }
  .rule-bottom { width: 300px; height: 1px; background: var(--rule); margin-top: 10px; }
</style>
</head>
<body>
  <section class="card card--front">
    <div class="brand">
      <span class="brand__dot"></span>
      <span class="brand__name">ALDERGATE CUSTOM HOMES</span>
    </div>
  </section>

  <section class="card card--back">
    <div class="frame" role="img" aria-label="Gold-to-black chevron foil border around the card"></div>
    <div class="details">
      <div class="details__name">DANIEL REYES</div>
      <div class="details__title">CEO/FOUNDER</div>
      <div class="divider">
        <span class="divider__line"></span>
        <div class="social">
          <span class="social__item"></span>
          <span class="social__item"></span>
          <span class="social__item"></span>
          <span class="social__item"></span>
          <span class="social__item"></span>
        </div>
        <span class="divider__line"></span>
      </div>
      <div class="details__address">412 Birchwood Court, Juneau, Alaska 99801</div>
      <div class="contact">
        <svg viewBox="0 0 10 10"><path d="M2 0.5 L3.6 2.6 L2.7 3.6 Q4 6 6.4 7.3 L7.4 6.4 L9.5 8 L8.3 9.5 Q3 8.5 0.5 1.7 Z"/></svg>
        <span>555 204 7719</span>
        <svg viewBox="0 0 10 10"><path d="M0.5 2 H9.5 V8 H0.5 Z M0.5 2 L5 5.5 L9.5 2" stroke="#f7f7f6" stroke-width="0.8"/></svg>
        <span>daniel@aldergatehomes.com</span>
        <svg viewBox="0 0 10 10"><circle cx="5" cy="5" r="4.5"/></svg>
        <span>www.aldergatehomes.com</span>
      </div>
      <div class="rule-bottom"></div>
    </div>
  </section>
</body>
</html>
```